Online travel site needs edgy website design

tripnook is the first Global Business Travel Website that provides the most comprehensive destination information tailored to suit the business traveller.

It is a ‘one click solution’ that offers direct access to all aspects of business travel, including general information on the city, accommodation and transportation options, economic and financial statistics, key business and services contacts, as well as leisure activities, entertainment suggestions, and listings for any personal needs.

Much more than a travel website, tripnook.com eliminates the need to buy multiple travel books or visit scores of websites. Most importantly, it is the only website that will cover such an extensive range of destinations around the world, while also featuring cities where information is really scarce. The user-friendly and consistent format for all destinations will allow the business traveller to easily navigate through more than 100 information pages on any destination.

tripnook will be simple to navigate, intuitive, unique in design, dynamic, and content rich providing a supreme user experience during navigation of the website.

The website will initially be English and is set to expand to more languages in the future.

A beta site with back-end database has been built - and now we need an edgy state of the art graphic design to reskin it.

LOOK & FEEL

Scope
The design of the site should reflect tripnook’s corporate and user centric philosophy with the following elements:

a. tripnook corporate image and branding
b. the promotion of each city destination
c. tripnook being the starting point of travel, while also a partner during travel
d. the subtle but powerful presence of advertising and sponsorship

All the above must derive from the design outline and elements that are going to be used.

Design Guidelines

Innovative and elegant design, minimalism, simplicity that permits the offering of the required information to be delivered in line with the values of Trust, Care, Discovery & Connection.

In addition:

1. The usability, navigation and the informative character of the corporate web site should not be compromised by the design.
2. The over-segmented pages and over-crowded content per page should be avoided.
3. The design should not only guide the user in an inviting way to the information required but also to intrigue them for further navigation.
4. Advertising space should be anticipated in line with the design character and OMR standard ad sizes.
5. The use of photos / videos should also encouraged.

Key Elements

a. Branding/Logos
Throughout the website branding should be present as a “guarantee seal” for the content accuracy. Corporate logo should be placed on every page while branding should also characterise any content element and/or tool. Appendix contains the current brand guidelines. Should additional sub-logos be required for specific sections, these should be proposed.

b. Fonts
Provided your experience on the website design you are requested to propose alternative font types and sizes always taken into consideration the inviting and user friendly character that the new website should aspire to. The font type that will be proposed must be user friendly in English typography, but also could support other languages in the future.

Given the fact that the majority of the text in the website contains information and listing, the fonts and text layout should not strain and fatigue the reader.

c. SEO
The design should be friendly towards the search engines.

d. Colours
Colour is considered as an integral part of the brand identity. Tripnook.com corporate colours are orange and grey as per the Attached document reference guide.

Different tonalities of the brand colours, or colours in general, should be proposed and applied, guided always by the above described scope of Look & Feel.

e. Section Headings
As presented above, the site’s section headings (refer Overview of the Site.) The principle is to label the content following users’ needs and mindset. However, the label space should be flexible for changes. The labels should facilitate the user to understand the content they host. This is important and should be applied especially to informative content.

Another function that Headings should perform is that of promoting the website’s content, especially when this kind of content will make the user spend more time in the website. This category of Headings should be approached in a more creative and attractive way as to intrigue users to check the content hosted.

f. Icons
Icons are considered necessary in order to provide the user extra help to guide them to reach the information they need quick n’ easy. Icons not only contribute actively to the creation of an attractive look & feel but, most importantly, facilitate navigation and speed up the users’ familiarisation with the website too.

Therefore their design should be eye-catching, comprehensive and dynamic, in accordance to the new site’s colour coding and following the latest trends as these were defined by the look & feel of smart phones.

PIXELHIVE BRIEF REQUIREMENTS
Based on the above, please provide at least two (2) approaches for the following pages – this includes colour palette in line with logo, layout, fonts.

Initial submissions can just address Deliverable 1 & 2 to fine tune design before proceeding further.

Please refer sample screenshots separately attached from raw beta site for content – available for Deliverables 2 -6.

(REFER example sites we like for their creativity: http://www.quillark-studio.co.uk/#Background, http://www.pelorafestas.com.br/, http://brambletondesign.co.uk/ )

Deliverable 1: Landing /Home page
- Access log in –
o Free Account or via WorkLattice/Chatterly etc
o Membership Access – Login
- How to use the site
- Allowance for video or animation
- Destination Selection
- Blog & Social media links

Deliverable 2: Destination Landing Page / Template
This is essentially a city guide template to be used for all cities throughout the site.

This page clearly depicts the four information sections
1. General
2. Business
3. Leisure
4. Personal

Also this page should include:
- Business News Feed
- Advertising & Sponsorship Spaces (according to OMR Standards)
- Destination Time, Weather, FX rates (LIVE feeds)
- Tips

Deliverable 3: Follow the above format but show an Internal Content Page – text only with subheadings

Deliverable 4: Follow the above format but show an Internal Content Page – text and photos

Deliverable 5: Follow the above format but show an Internal Content Page – Listing Sections such as Restaurants (this must also include filter categories)

Deliverable 6: Follow the above format but show an Internal Content Page – Top 10 Experiences – this incorporates address and contact details, photo and sub-text

Deliverable 7: The Membership Landing Page which should include:
1. Intro
2. Advertising & Sponsorship Space
3. The four sections
4. Tips Section
Updates

Hi all - just to reiterate that we are open to different approaches in the design.  We only included the existing screen shots of the beta site to provide you with an idea of the content.  We definitely don't want to see anything similar.....we want it to be edgy yet simple and easy to navigate....we want to create an outstanding user experience!  Cheers Tripnook Team

Reason: Dear Designers - We are extending the period as have not had many submissions at all and want to provide more time. If you have already submitted, we will be in touch shortly with feedback. Thanks for your understanding Tripnook Team

Reason: We would like to give everyone more time so we can find the best and most preferred design.

Target Market(s)

TARGET MARKET
tripnook is a consumer focused website, offering a wide-range of easy-to-use and interactive platforms, for informative and commercial purposes, while also providing attractive and innovative advertising real-estate for potential business partners.

The target audience can be segmented as follows:

Primary Target: Professionals travelling on Business

They require up-to-date reliable information prior and during their travel, as well as facilitation to take action. They need an online Personal Assistant.

The personal characteristics of the primary target group are: busy life, tailored solutions, reliable sources, trusting, caring, and spoiled.
 
The website will have a membership option (for a small annual fee) which will provide customized information for their demographic and preferences. Sub target groups will include:
1. Business Men 40 years
3. Business Women 40 years
5. Business People with reduced mobility

Demographic & Travelling Profile of Business Travellers

• 92% of them use the internet as a source of info
• 54% are males, 38 years old
• 80% holds a college/university degree
• 68% is travelling mainly for leisure and annually 6 times per year
• 52% reserve their ticket through the internet
• 66% is travel internationally

Secondary Targets:

Executive PA’s
Executive personal assistants who need to plan their manager’s travel and provide support information for their trip.

Professionals travelling for Leisure and Partners
They have most probably used the website for their business travel, but consider it also useful for their leisure travel. The generic website, will include enough information to cover most of the leisure needs, as well as the requirements of their partners.

Direct Business-to-Business [B2B] Targets
The direct [B2B] targeted audience includes corporations that would like to use a white label solution for their staff, by using all available destinations or a selected number depending on their global network.

Business-to-Business [B2B] Targets
The [B2B] targeted audience is an indirect audience, for which tripnook promotes its services, and a key revenue stream. The B2B audience consists mainly of a diverse range of professional organisations targeting the business traveller (airlines, hotels, travel agencies, tourism authorities, entertainment companies, services, etc.) tripnook will be targeting these organisations to advertise on the site.
 
Desired Response from Target Groups

The desired response from the consumer targets is:
a) Recurrent use of website
b) Share content/experience with friends and social networking sites
c) Interact on the website’s Blog
d) Register for newsletters and offers
e) Subscribe to Membership
f) Be exposed to commercial advertisements on the website
g) Provide feedback (in the future) for services
h) Use (in the future) online services to purchase products and services
Competition

Industry/Entity Type

Travel

Requirements
Must have
• A clean crisp and professional appearance giving a sense of Trust and Reliability.
Should not have
• It should not look like every other run of the mill travel sites - Roomvale.com, Jaunteo etc

```html
<!DOCTYPE html>
<html lang="en">
<head>
<meta charset="utf-8">
<title>tripnook — Business Travel</title>
<link href="https://fonts.googleapis.com/css2?family=Lato:wght@400;700&family=Arimo:wght@400;700&display=swap" rel="stylesheet">
<style>
:root{
  --orange:#e8782a;
  --orange-light:#f39345;
  --orange-dark:#d9661a;
  --ink:#2b2b2b;
  --text:#555;
  --muted:#8a8a8a;
  --rule:#d8d8d8;
  --band:#e7e6e3;
  --bar:#555555;
  --footer:#363636;
  --footer-head:#9a9a9a;
  --white:#fff;
}
*{box-sizing:border-box;margin:0;padding:0}
html,body{width:1200px;height:2200px;overflow:hidden;background:var(--white)}
body{position:relative;font-family:"Lato",sans-serif;color:var(--text)}
.abs{position:absolute}

/* header */
.site-header{position:absolute;left:0;top:0;width:1200px;height:73px;background:linear-gradient(#f39548,#e06f20);}
.brand{position:absolute;left:129px;top:14px;display:flex;align-items:center;gap:10px}
.brand-dot{width:38px;height:38px;border-radius:50%;background:#fff;opacity:.9}
.brand-name{font-size:34px;font-weight:700;color:#fff;letter-spacing:.5px}
.main-nav{position:absolute;left:378px;top:0;height:73px;display:flex}
.main-nav a{display:block;height:73px;line-height:70px;padding:0 20px;color:#fff;font-size:15px;text-decoration:none;border-left:1px solid rgba(255,255,255,.25)}
.main-nav a:last-child{border-right:1px solid rgba(255,255,255,.25)}
.account{position:absolute;left:772px;top:21px;display:flex;align-items:center;gap:14px;font-size:14px;color:#fff}
.btn-register{background:#5a5a5a;border-radius:3px;padding:5px 14px;font-size:12px}
.btn-chatterly{background:#4f6aa8;border-radius:3px;padding:5px 12px;font-size:12px}
.lang{display:flex;align-items:center;gap:6px}

/* hero */
.hero-photo{position:absolute;left:0;top:73px;width:1200px;height:514px;background:linear-gradient(100deg,#d7dcdf 0%,#eef1f2 30%,#8a8e93 40%,#3a3c40 48%,#c9ccd0 60%,#f4f4f4 75%,#fbfbfb 100%)}
.search-panel{position:absolute;left:298px;top:283px;width:603px;height:135px;background:rgba(60,60,60,.85);border-radius:4px}
.search-title{position:absolute;left:0;top:14px;width:603px;text-align:center;color:#fff;font-size:24px;font-weight:700}
.search-title em{font-style:normal;color:var(--orange-light);font-size:31px}
.search-field{position:absolute;left:14px;top:60px;width:520px;height:56px;background:#fff;padding-left:20px;line-height:56px;color:#999;font-size:17px}
.search-btn{position:absolute;left:534px;top:60px;width:56px;height:56px;background:var(--orange);display:flex;align-items:center;justify-content:center}

/* destinations */
.destinations{position:absolute;left:0;top:587px;width:1200px;height:377px;background:var(--band)}
.section-bar{position:absolute;left:116px;top:26px;width:965px;height:57px;background:var(--bar);color:#fff;font-size:26px;text-align:center;line-height:57px;border-radius:2px}
.section-bar::after{content:"";position:absolute;left:474px;bottom:-9px;border:9px solid transparent;border-bottom:0;border-top-color:var(--bar)}
.carousel-arrow{position:absolute;top:129px;width:34px;height:208px;background:#cfcbc8;display:flex;align-items:center;justify-content:center}
.dest-card{position:absolute;top:129px;width:201px;height:208px;background:#fff;overflow:hidden}
.dest-photo{height:142px}
.ribbon{position:absolute;left:-30px;top:18px;width:110px;transform:rotate(-45deg);background:var(--orange);color:#fff;font-size:10px;text-align:center;padding:3px 0;letter-spacing:.5px}
.heart{position:absolute;right:6px;top:4px}
.dest-name{font-size:13px;font-weight:700;color:#333;padding:15px 12px 4px;white-space:nowrap;overflow:hidden}
.dest-place{font-size:12.5px;color:var(--orange);padding:0 12px;display:flex;gap:5px;align-items:center}

/* content */
.block-title{position:absolute;font-size:20px;color:var(--ink);border-bottom:1px solid var(--rule);padding-bottom:8px}
.block-title em{font-style:normal;color:var(--orange)}
.intro-text{position:absolute;left:129px;top:1050px;width:594px;font-size:12.5px;line-height:22.5px;color:#444}
.btn-orange{position:absolute;background:var(--orange);color:#fff;font-size:13px;display:flex;align-items:center;justify-content:center;border-radius:2px}
.video{position:absolute;left:763px;top:1053px;width:316px;height:184px;background:linear-gradient(160deg,#5a6066 0%,#8d9196 35%,#c9c9c6 55%,#6c7068 80%,#3d423e 100%)}
.video-title{position:absolute;left:46px;top:8px;background:#1b6fa8;color:#fff;font-size:10px;padding:3px 6px}
.video-sub{position:absolute;left:46px;top:25px;color:#ddd;font-size:8px}
.video-bar{position:absolute;left:0;bottom:0;width:316px;height:22px;background:rgba(0,0,0,.75)}
.video-play{position:absolute;left:8px;top:3px;width:34px;height:16px;background:#222;display:flex;align-items:center;justify-content:center}
.video-track{position:absolute;left:60px;top:9px;width:200px;height:4px;background:#555}
.video-track span{display:block;width:90px;height:4px;background:#1ea0e0}

.post-photo{position:absolute;left:129px;width:163px;height:142px;border:1px solid #ddd}
.post-title{position:absolute;left:317px;font-size:16px;color:#222}
.post-text{position:absolute;left:317px;width:410px;font-size:11.5px;line-height:20px;color:#555}
.read-more{position:absolute;left:320px;font-size:13px;color:#222;display:flex;align-items:center;gap:10px}
.read-more i{width:16px;height:16px;border-radius:50%;background:var(--orange);display:inline-block;position:relative}
.read-more i::after{content:"";position:absolute;left:4px;top:7px;width:8px;height:2px;background:#fff}
.post-meta{position:absolute;left:320px;font-size:11px;color:#666;display:flex;gap:14px;align-items:center}
.share{position:absolute;left:127px;display:flex;gap:8px}
.share span{width:15px;height:15px;border-radius:2px;background:#6fa9c9}
.share span+span{background:#4f6aa8}
.divider{position:absolute;left:129px;width:590px;height:1px;background:var(--rule)}

.widget{position:absolute;left:772px;width:300px;background:#fff;border:1px solid #e2e2e2;box-shadow:0 0 0 4px #f1f1f1}
.widget.login{top:1294px;height:185px;background:#f4f4f4}
.widget h3{font-size:15px;font-weight:400;color:#222;position:absolute;left:15px}
.field{position:absolute;left:15px;width:268px;height:28px;background:#fff;border:1px solid #d3d3d3;font-size:11px;color:#888;padding-left:12px;line-height:26px}
.widget.fans{top:1507px;height:309px}
.fan-name{position:absolute;left:75px;top:54px;color:#3b5998;font-size:14px}
.fan-avatar{position:absolute;left:15px;top:54px;width:50px;height:50px;background:linear-gradient(#2c3e63,#8a6a4a)}
.fan-like{position:absolute;left:75px;top:78px;font-size:11px;color:#3b5998;border:1px solid #c6cde0;background:#eef0f6;padding:2px 6px}
.fan-count{position:absolute;left:15px;top:120px;font-size:11px;color:#333;border-top:1px solid #e4e4e4;width:268px;padding-top:6px}
.fan-count b{color:#3b5998;font-weight:400;margin-left:6px}
.fan-grid{position:absolute;left:15px;top:145px;width:265px;height:101px;background:linear-gradient(120deg,#8a6b55,#c9a07a 30%,#7f8a5a 55%,#b87a5c 80%,#6a6a70)}
.fan-foot{position:absolute;left:15px;top:258px;width:268px;border-top:1px solid #e4e4e4;padding-top:6px;font-size:9px;color:#777;display:flex;gap:6px;align-items:center}
.fan-foot i{width:10px;height:10px;background:#3b5998;display:inline-block}

/* footer */
.site-footer{position:absolute;left:0;top:1853px;width:1200px;height:347px;background:var(--footer);font-family:"Arimo",sans-serif}
.foot-col{position:absolute;top:46px}
.foot-col h4{font-size:19px;color:var(--footer-head);font-weight:700;margin-bottom:12px}
.foot-col li{list-style:none;font-size:13.5px;color:#fff;line-height:22px;display:flex;align-items:center;gap:8px}
.foot-col li.accent{color:var(--orange)}
.sq{width:13px;height:13px;border-radius:2px;display:inline-block}
.copyright{position:absolute;left:134px;top:296px;font-size:12.5px;color:#ddd}
.foot-lang{position:absolute;left:963px;top:292px;color:#fff;font-size:15px;display:flex;gap:6px;align-items:center}
</style>
</head>
<body>

<header class="site-header">
  <div class="brand"><span class="brand-dot"></span><span class="brand-name">tripnook</span></div>
  <nav class="main-nav">
    <a>Home</a><a>Destination</a><a>Blog</a><a>Contact Us</a>
  </nav>
  <div class="account">
    <span class="btn-register">Register</span>
    <span>Log In</span>
    <span class="btn-chatterly">Chatterly</span>
    <span class="lang">
      <svg width="22" height="22" viewBox="0 0 22 22"><circle cx="11" cy="11" r="10" fill="#fff"/><path d="M5 7c3 0 4 2 3 4s1 4 0 6M14 3c-1 3 2 4 4 4M13 13c2 0 3 2 2 5" stroke="#e8782a" stroke-width="1.6" fill="none"/></svg>
      English
    </span>
  </div>
</header>

<section class="hero">
  <div class="hero-photo" role="img" aria-label="Photo of two business travellers with suitcases reading a document in a bright airport terminal"></div>
  <div class="search-panel">
    <div class="search-title">Search <em>50,000</em> + Places in <em>142</em> countries</div>
    <div class="search-field">Where you want to go?</div>
    <div class="search-btn"><svg width="24" height="24" viewBox="0 0 24 24"><circle cx="10" cy="10" r="7" stroke="#fff" stroke-width="3" fill="none"/><path d="M15 15l6 6" stroke="#fff" stroke-width="3.5" stroke-linecap="round"/></svg></div>
  </div>
</section>

<section class="destinations">
  <div class="section-bar">Hot Destinations</div>
  <div class="carousel-arrow" style="left:116px"><svg width="12" height="18"><path d="M10 2L3 9l7 7" stroke="#555" stroke-width="3" fill="none"/></svg></div>
  <div class="carousel-arrow" style="left:1048px"><svg width="12" height="18"><path d="M2 2l7 7-7 7" stroke="#555" stroke-width="3" fill="none"/></svg></div>

  <article class="dest-card" style="left:170px">
    <div class="dest-photo" role="img" aria-label="Photo of a villa garden with a swimming pool" style="background:linear-gradient(#6b8fa8,#3e6b3e 45%,#3aa0b8 70%,#7a6a52)"></div>
    <span class="ribbon">LATEST</span>
    <svg class="heart" width="16" height="14" viewBox="0 0 16 14"><path d="M8 13S1 8.5 1 4.5A3.5 3.5 0 018 3a3.5 3.5 0 017 1.5C15 8.5 8 13 8 13z" fill="#fff" opacity=".85"/></svg>
    <div class="dest-name">Maison ensoleillée avec t...</div>
    <div class="dest-place"><svg width="8" height="11"><path d="M4 11S0 6 0 4a4 4 0 018 0c0 2-4 7-4 7z" fill="#e8782a"/></svg>London, United Kingdom</div>
  </article>
  <article class="dest-card" style="left:390px">
    <div class="dest-photo" role="img" aria-label="Photo of a blue alpine lake between green mountains" style="background:linear-gradient(#8fb3d0,#6a8a5a 35%,#1d5a8a 60%,#3d6e3a)"></div>
    <span class="ribbon">LATEST</span>
    <svg class="heart" width="16" height="14" viewBox="0 0 16 14"><path d="M8 13S1 8.5 1 4.5A3.5 3.5 0 018 3a3.5 3.5 0 017 1.5C15 8.5 8 13 8 13z" fill="#fff" opacity=".85"/></svg>
    <div class="dest-name">Sarnen (near Lucerne an...</div>
    <div class="dest-place"><svg width="8" height="11"><path d="M4 11S0 6 0 4a4 4 0 018 0c0 2-4 7-4 7z" fill="#e8782a"/></svg>New York, United States</div>
  </article>
  <article class="dest-card" style="left:610px">
    <div class="dest-photo" role="img" aria-label="Photo of footprints in beach sand" style="background:linear-gradient(135deg,#b9aa98,#9d8e7c 50%,#c3b5a3)"></div>
    <span class="ribbon">LATEST</span>
    <svg class="heart" width="16" height="14" viewBox="0 0 16 14"><path d="M8 13S1 8.5 1 4.5A3.5 3.5 0 018 3a3.5 3.5 0 017 1.5C15 8.5 8 13 8 13z" fill="#fff" opacity=".85"/></svg>
    <div class="dest-name">Cosy holiday home close ...</div>
    <div class="dest-place"><svg width="8" height="11"><path d="M4 11S0 6 0 4a4 4 0 018 0c0 2-4 7-4 7z" fill="#e8782a"/></svg>Miami Beach</div>
  </article>
  <article class="dest-card" style="left:830px">
    <div class="dest-photo" role="img" aria-label="Photo of a dining room with large windows" style="background:linear-gradient(#d8d2c4,#8a7660 55%,#5a4a3a)"></div>
    <span class="ribbon">LATEST</span>
    <svg class="heart" width="16" height="14" viewBox="0 0 16 14"><path d="M8 13S1 8.5 1 4.5A3.5 3.5 0 018 3a3.5 3.5 0 017 1.5C15 8.5 8 13 8 13z" fill="#fff" opacity=".85"/></svg>
    <div class="dest-name">Beautiful house in Amste...</div>
    <div class="dest-place"><svg width="8" height="11"><path d="M4 11S0 6 0 4a4 4 0 018 0c0 2-4 7-4 7z" fill="#e8782a"/></svg>Amsterdam</div>
  </article>
</section>

<main>
  <h2 class="block-title" style="left:129px;top:990px;width:590px">How to Use <em>Tripnook</em></h2>
  <p class="intro-text">Lorem Ipsum is simply dummy text of the printing and typesetting industry. Lorem Ipsum has been the industry's standard dummy text ever since the 1500s, when an unknown printer took a galley of type and scrambled it to make a type specimen book. It has survived not only five centuries, but also the leap into electronic typesetting, remaining essentially unchanged.Lorem Ipsum is simply dummy text of the printing and typesetting industry. Lorem Ipsum has been the industry's standard dummy text ever since the 1500s, when an unknown printer took a galley of type and scrambled it to make a type specimen book. It has</p>
  <span class="btn-orange" style="left:129px;top:1206px;width:93px;height:34px">Read More</span>

  <h2 class="block-title" style="left:763px;top:990px;width:316px">Our Video</h2>
  <div class="video" role="img" aria-label="Video still of a white hillside citadel beneath mountains">
    <span class="video-title">Place Title For Movie Here</span>
    <span class="video-sub">from Your Channel</span>
    <div class="video-bar">
      <span class="video-play"><svg width="8" height="9"><path d="M0 0l8 4.5L0 9z" fill="#fff"/></svg></span>
      <span class="video-track"><span></span></span>
    </div>
  </div>

  <h2 class="block-title" style="left:133px;top:1295px;width:586px">Our Blog</h2>

  <article>
    <div class="post-photo" style="top:1366px;background:linear-gradient(#3d6fb0,#d8dde2 40%,#6a6a66 70%,#4aa0a8)" role="img" aria-label="Photo of snowy mountains above a glacier lake"></div>
    <h3 class="post-title" style="top:1367px">Lorem Ipsum Dolor</h3>
    <p class="post-text" style="top:1393px">Lorem Ipsum is simply dummy text of the printing and typesetting industry. Lorem Ipsum has been the iLorem Ipsum is simply dummy text of the printing and typesetting industry. Lorem Ipsum has been the industry's</p>
    <span class="read-more" style="top:1464px">Read More <i></i></span>
    <div class="share" style="top:1540px"><span></span><span></span></div>
    <div class="post-meta" style="top:1524px"><span>◷ 12 September 2013</span><span>▭ Destination: Thailand</span></div>
    <div class="divider" style="top:1577px"></div>
  </article>

  <article>
    <div class="post-photo" style="top:1611px;background:linear-gradient(#7aa6d8,#c9d4e0 35%,#6a5a4a 60%,#a08a6a)" role="img" aria-label="Photo of a gothic bridge tower and old town rooftops"></div>
    <h3 class="post-title" style="top:1621px">Lorem Ipsum Dolor</h3>
    <p class="post-text" style="top:1647px">Lorem Ipsum is simply dummy text of the printing and typesetting industry. Lorem Ipsum has been the iLorem Ipsum is simply dummy text of the printing and typesetting industry. Lorem Ipsum has been the industry's</p>
    <span class="read-more" style="top:1718px">Read More <i></i></span>
    <div class="share" style="top:1785px"><span></span><span></span></div>
    <div class="post-meta" style="top:1783px"><span>◷ 13 Spetember 2013</span><span>▭ Destination: China</span></div>
    <div class="divider" style="top:1819px"></div>
  </article>

  <aside class="widget login">
    <h3 style="top:26px">MEMBERSHIP LOGIN</h3>
    <div class="field" style="top:58px">email</div>
    <div class="field" style="top:97px">password</div>
    <span class="btn-orange" style="left:18px;top:143px;width:64px;height:27px">Login</span>
  </aside>

  <aside class="widget fans">
    <h3 style="top:14px">CHATTERLY FAN PAGE</h3>
    <div class="fan-avatar" role="img" aria-label="Page profile picture"></div>
    <span class="fan-name">Tripnook</span>
    <span class="fan-like">Like</span>
    <div class="fan-count">2,021 people like<b>Tripnook</b></div>
    <div class="fan-grid" role="img" aria-label="Grid of small fan profile pictures"></div>
    <div class="fan-foot"><i></i>Chatterly social plugin</div>
  </aside>
</main>

<footer class="site-footer">
  <div class="foot-col" style="left:136px"><h4>Company</h4><ul><li>About</li><li>Contact Us</li><li>Meet Our Team</li><li>Newsroom</li><li>Blog</li><li>Privacy Policy</li><li>Terms of Use</li></ul></div>
  <div class="foot-col" style="left:356px"><h4>Help</h4><ul><li>How It Works</li><li>Help Center</li><li>Getting Started</li><li>Community Guidelines</li><li>Is Home Swapping Safe?</li></ul></div>
  <div class="foot-col" style="left:576px"><h4>Useful Links</h4><ul><li>Pricing &amp; Benefits</li><li>Member Stories</li><li>Travel Resources</li><li>Known Issues</li><li style="margin-top:20px">Already a Member of</li><li>Tripnook ?</li><li class="accent">Get our Special Offer!</li></ul></div>
  <div class="foot-col" style="left:797px"><h4>Follow Us</h4><ul>
    <li><span class="sq" style="background:#4f6aa8"></span>Chatterly</li>
    <li><span class="sq" style="background:#4aa3d8"></span>Chirpline</li>
    <li><span class="sq" style="background:#c9302c"></span>Pinboardly</li>
    <li><span class="sq" style="background:#555"></span>Circlefeed</li></ul></div>
  <div class="foot-col" style="left:961px"><h4>Get Started</h4><ul><li>Not a Member yet?</li><li class="accent">Join Now!</li></ul></div>
  <p class="copyright">© Tripnook.com™ All Rights Reserved.</p>
  <div class="foot-lang"><svg width="18" height="18" viewBox="0 0 22 22"><circle cx="11" cy="11" r="10" fill="#fff"/><path d="M5 7c3 0 4 2 3 4s1 4 0 6M14 3c-1 3 2 4 4 4M13 13c2 0 3 2 2 5" stroke="#363636" stroke-width="1.6" fill="none"/></svg>English</div>
</footer>

</body>
</html>
```